Bridal Beauty Expert 5 page Website

Modern 5 page website including: home page, Bridal Experts, services, gallery, and book me. Home page to include photo slideshow and contact information for stylist. The Bridal a Experts section will include short biography and photos of each bridal expert 3-4. Services page will include list and description of services and pricing. Gallery will contain work divided in the hair and makeup category. The book me page will contain an active booking tab with drop down service and customer information.

Target Market(s)

Brides, ages 21 to 45

Industry/Entity Type

Hair And Beauty

Coding

Coded - Design and coding required

Number of Pages Required

5+ page

Font styles to use
Serif
Decorative
Script

Colors
faa54b
97b8d9

Requirements
Must have
• Photo slideshow, photo gallery
Nice to have
• Scrolling slide show on home page

```html
<!DOCTYPE html>
<html lang="en">
<head>
<meta charset="utf-8">
<title>Mara Ellison – Master Stylist | Veil &amp; Bloom</title>
<link href="https://fonts.googleapis.com/css2?family=Arimo:wght@400;700&display=swap" rel="stylesheet">
<style>
  :root {
    --blue: #97b8d9;
    --orange: #faa54b;
    --nav-blue: #8fb2d8;
    --teal: #3cc8c0;
    --body-text: #6b6b6b;
    --white: #ffffff;
    --frame-border: #e2e2e2;
    --photo-light: #e9ecef;
    --photo-dark: #9aa3ab;
  }
  * { margin: 0; padding: 0; box-sizing: border-box; }
  html, body { width: 1200px; height: 747px; overflow: hidden; background: var(--white); }
  body { position: relative; font-family: "Arimo", Arial, sans-serif; }

  .brand {
    position: absolute; left: 188px; top: 46px; width: 196px;
    text-align: center; color: var(--teal); font-size: 24px; font-weight: 400;
  }
  .main-nav {
    position: absolute; top: 58px; left: 0; width: 1200px; height: 20px;
  }
  .main-nav a {
    position: absolute; top: 0; font-size: 14px; color: var(--nav-blue);
    text-decoration: none; letter-spacing: 0.2px;
  }
  .main-nav a.is-current { color: var(--orange); }
  .page-title {
    position: absolute; top: 91px; left: 409px; width: 600px;
    text-align: center; font-size: 21px; font-weight: 400; color: var(--nav-blue);
  }
  .page-title span { color: var(--orange); }

  .portrait-frame {
    position: absolute; left: 182px; top: 141px; width: 333px; height: 507px;
    background: var(--white); border: 1px solid var(--frame-border);
    box-shadow: 0 10px 10px -6px rgba(0,0,0,0.35);
  }
  .portrait {
    position: absolute; left: 6px; top: 6px; width: 319px; height: 493px;
    background: linear-gradient(160deg, var(--photo-light) 0%, #cdd3d8 45%, var(--photo-dark) 75%, var(--photo-light) 100%);
  }

  .bio { position: absolute; left: 548px; top: 152px; width: 458px; }
  .bio-name {
    text-align: center; font-size: 32px; font-weight: 400; color: var(--nav-blue);
    line-height: 38px;
  }
  .bio-role {
    text-align: center; font-size: 22px; font-weight: 400; color: var(--orange);
    line-height: 26px; margin-top: 4px;
  }
  .bio-text { margin-top: 21px; }
  .bio-text p {
    font-size: 10.3px; line-height: 12.8px; color: var(--body-text);
    margin-bottom: 12.8px;
  }

  .site-footer {
    position: absolute; left: 0; top: 665px; width: 1200px; height: 82px;
    background: var(--blue);
  }
  .site-footer .rule {
    position: absolute; left: 0; width: 1200px; height: 2px; background: var(--white);
  }
  .footer-item {
    position: absolute; top: 31px; font-size: 13px; color: var(--white); line-height: 16px;
    white-space: nowrap;
  }
  .footer-divider {
    position: absolute; top: 22px; width: 1px; height: 32px; background: rgba(255,255,255,0.6);
  }
  .social-dot {
    position: absolute; top: 28px; width: 21px; height: 21px; border-radius: 50%;
    background: rgba(255,255,255,0.55);
  }
</style>
</head>
<body>
  <header>
    <div class="brand">Veil &amp; Bloom</div>
    <nav class="main-nav">
      <a href="#" style="left:462px">HOME</a>
      <a href="#" class="is-current" style="left:556px">ABOUT ME</a>
      <a href="#" style="left:667px">SERVICES</a>
      <a href="#" style="left:778px">GALLERY</a>
      <a href="#" style="left:885px">BOOK ME</a>
    </nav>
    <h2 class="page-title">MARA ELLISON - <span>MASTER STYLIST</span></h2>
  </header>

  <main>
    <figure class="portrait-frame">
      <div class="portrait" role="img" aria-label="Portrait of the stylist in a white dress standing in a bright glass walkway"></div>
    </figure>

    <section class="bio">
      <h1 class="bio-name">MARA ELLISON</h1>
      <h3 class="bio-role">MASTER STYLIST</h3>
      <div class="bio-text">
        <p>A professional stylist for over five years, Mara Ellison possess a great deal of passion for the world of beauty and believes that hair is a women's most prized ornament. As a hair artist, ninety percent of her direction with a hairstyle comes from the hair and the other ten percent from the client's request. Ellison attributes her diverse technique and styling ability to her Lumen Academy education and rich culture.</p>
        <p>The child of West African immigrants, Ellison was exposed to the world of hair while watching her mother earn extra money braiding in their Staten Island, NY community. While most seven year olds were outside playing, Marisol "Mara" Ellison mastered the technique of adding synthetic hair extensions to her dolls hair. Although she was the "kitchen beautician" for her peers throughout middle school and high school, Mara's dreams of becoming a famous hairstylist were plagued by the cultural misconception that this line of work was not prestigious enough, so instead she attended Northfield State University for a B.A. in Marketing.</p>
        <p>After turning to her God given talents when she ran into some financial issues, Ellison realized the industry was missing her skill and passion for healthy hair. Mara Ellison took reigns on her life and success by deciding to leave corporate America in 2011; and she hasn't looked backed since. Her work has graced the pages of fashion magazines and runways for designers, such as a televised fashion competition contestant Adaeze Lane. Continuing to grow her brand, Ellison recently opened a private salon suite and a bridal sector called "Veil &amp; Bloom" The Bridal Hair Experts.</p>
      </div>
    </section>
  </main>

  <footer class="site-footer">
    <div class="rule" style="top:11px"></div>
    <div class="rule" style="top:66px"></div>
    <span class="footer-item" style="left:218px">(555) 014-2238</span>
    <span class="footer-divider" style="left:326px"></span>
    <span class="footer-item" style="left:342px">Email: hi@veilbloom.com</span>
    <span class="footer-divider" style="left:496px"></span>
    <span class="social-dot" style="left:513px"></span>
    <span class="social-dot" style="left:548px"></span>
    <span class="social-dot" style="left:583px"></span>
    <span class="footer-divider" style="left:623px"></span>
    <span class="footer-item" style="left:637px">410 Magnolia Ave Suite 12, Fairhaven, Georgia 30000</span>
  </footer>
</body>
</html>
```